Dental Medical History Form - Content provided

Design a medical history form for a dental practice. Content is provided so all that is needed is the formatting to make it look great and easy to read.

"Patient Information" to include all information contained in top portion of the "Patient Medical History Form" docx file.

"Medical History" should follow the formatting and content of the "Exact Medical History" file as this is what the entry fields look like in our practice software and so we would like it to match.

1st page - Patient info, allergies, medications, antibiotics, joint replacement, pregnancy.

2nd page - Do you have, or have you had, any of the following? . . . . . . .
Updates

Project Deadline Extended Reason: Picked too short of a deadline to start (2 days) Added Monday, February 13, 2017

Target Market(s)

All ages but must be clear enough for elderly to read. Use as much space as possible to keep font size bigger yet keep to two pages

Industry/Entity Type

Dental

Font styles to use
Sans Serif

Requirements
Must have
• All content provided
• Our logo at the top (file provided)
• Century Gothic Font
• Limit to two pages

```html
<!DOCTYPE html>
<html lang="en">
<head>
<meta charset="utf-8">
<title>Harbourline Dental – Confidential Medical History</title>
<link href="https://fonts.googleapis.com/css2?family=Questrial&family=Mulish:wght@700;800&display=swap" rel="stylesheet">
<style>
  :root{
    --bg:#eeefef;
    --paper:#ffffff;
    --ink:#1d1f20;
    --muted:#55595c;
    --brand:#4a5157;
    --field:#e2e6e7;
    --box:#dde1e2;
  }
  *{box-sizing:border-box;margin:0;padding:0}
  html,body{width:1200px;height:1200px;overflow:hidden}
  body{background:var(--bg);font-family:"Questrial",sans-serif;color:var(--ink);position:relative}
  .page{position:absolute;top:197px;width:570px;height:806px;background:var(--paper);
        box-shadow:0 2px 10px rgba(0,0,0,.12);padding:38px 36px;font-size:10.5px}
  .page--info{left:20px}
  .page--history{left:610px}
  .bold{font-family:"Mulish",sans-serif;font-weight:800}
  .field{display:block;height:13px;background:var(--field);flex:1}
  .box{display:inline-block;width:10px;height:10px;background:var(--box);vertical-align:-1px;margin:0 6px 0 3px}

  /* page 1 */
  .letterhead{display:flex;justify-content:space-between;align-items:flex-end;margin-bottom:34px}
  .brand{font-size:30px;color:var(--brand);line-height:1;display:flex;align-items:center;gap:8px}
  .brand-mark{width:12px;height:12px;background:var(--brand)}
  .practice-address{font-size:12.5px;line-height:1.5;color:var(--ink)}
  .form-title{text-align:center;font-size:19px;letter-spacing:.5px;margin-bottom:22px}
  .details{display:grid;grid-template-columns:1fr 1fr;gap:22px;margin-bottom:20px}
  .row{display:flex;align-items:center;gap:5px;margin-bottom:5px;white-space:nowrap}
  .row .label{min-width:56px}
  .sublabels{display:flex;justify-content:space-around;font-size:8px;color:var(--muted);margin:-3px 0 6px 60px}
  .gap{height:10px}
  .section-q{font-size:11.5px;margin:14px 0 8px}
  .choices{display:flex;flex-wrap:wrap;gap:6px 12px;font-size:11.5px;margin-bottom:6px}
  .med-fields{display:grid;grid-template-columns:1fr 1fr;gap:9px 18px;margin-bottom:20px}
  .med-fields .field{height:14px}
  .yn-row{display:flex;justify-content:space-between;align-items:center;margin-bottom:9px;font-size:11.5px}
  .women{margin-top:16px;font-size:11.5px}

  /* page 2 */
  .history-q{font-size:12px;margin-bottom:14px}
  .columns{display:grid;grid-template-columns:1fr 1fr;gap:26px}
  .group{margin-bottom:12px}
  .group h3{font-family:"Mulish",sans-serif;font-weight:800;font-size:10.5px;margin-bottom:4px}
  .item{display:flex;justify-content:space-between;align-items:center;height:16.5px}
  .item .yn{white-space:nowrap;font-size:10px}
  .other-line{display:flex;gap:6px;align-items:center;margin-top:4px}
  .sign{margin-top:10px;width:58%}
  .sign .row{margin-bottom:8px}
  .thanks{margin-top:14px;font-size:9px;line-height:1.35;color:var(--muted)}
</style>
</head>
<body>

<section class="page page--info">
  <header class="letterhead">
    <div class="brand"><span>harbourline dental</span><span class="brand-mark"></span></div>
    <address class="practice-address" style="font-style:normal">
      Harbourline Dental<br>Suite 4/18 Lakeview Rd<br>Tarrin NSW 2261<br>(02) 4000 1234
    </address>
  </header>

  <h1 class="form-title" style="font-weight:400">CONFIDENTIAL MEDICAL HISTORY</h1>

  <div class="details">
    <div class="patient">
      <div class="row"><span class="label">Name:</span><span class="field"></span></div>
      <div class="sublabels"><span>Title</span><span>First</span><span>Middle</span><span>Last</span></div>
      <div class="row"><span class="label">Address:</span><span class="field"></span></div>
      <div class="row"><span class="label">DOB:</span><span class="field"></span></div>
      <div class="row"><span class="label">Email Address:</span><span class="field"></span></div>
      <div class="row"><span class="label">Phone Number(s):</span><span class="field"></span></div>
      <div class="sublabels" style="margin-left:110px"><span>Mobile</span><span>Work</span><span>Home</span></div>
      <div class="gap"></div>
      <div class="row">Emergency Contact Person:</div>
      <div class="row"><span class="label">Name:</span><span class="field"></span></div>
      <div class="row"><span class="label">Relationship:</span><span class="field"></span></div>
      <div class="row"><span class="label">Phone number:</span><span class="field"></span></div>
    </div>
    <div class="practice">
      <div class="row">General Practitioner:</div>
      <div class="row"><span class="label">Name:</span><span class="field"></span></div>
      <div class="row"><span class="label">Practice Name:</span><span class="field"></span></div>
      <div class="row"><span class="label">Phone Number:</span><span class="field"></span></div>
      <div class="gap"></div>
      <div class="row">Do you have a health fund?</div>
      <div class="row">Yes<span class="box"></span>or No<span class="box"></span></div>
      <div class="row">If so, what is the name of your fund?</div>
      <div class="row"><span class="label">Fund Number?</span><span class="field"></span></div>
      <div class="row"><span class="label">Priority Number on card:</span><span class="field"></span></div>
      <div class="row"><span class="label">Occupation:</span><span class="field"></span></div>
      <div class="row"><span class="label">Referred by:</span><span class="field"></span></div>
    </div>
  </div>

  <p class="section-q bold">Please indicate if you are allergic to any of the following ✓?</p>
  <div class="choices">
    <span>Aspirin<span class="box"></span></span><span>Codeine<span class="box"></span></span>
    <span>Penicillin<span class="box"></span></span><span>Sulfites<span class="box"></span></span>
    <span>Latex<span class="box"></span></span><span>Local Anaesthetic<span class="box"></span></span>
  </div>
  <div class="row" style="font-size:11.5px">Other<span class="field" style="height:15px"></span></div>

  <p class="section-q bold">Are you currently taking, or have ever taken, any of the following?</p>
  <div class="choices">
    <span>Asthma inhaler<span class="box"></span></span><span>Anti-epileptics<span class="box"></span></span>
    <span>Anti-depressants<span class="box"></span></span><span>Blood thinners<span class="box"></span></span>
    <span>Bisphosphonates<span class="box"></span></span><span>Chemotherapy<span class="box"></span></span>
    <span>Insulin<span class="box"></span></span><span>Immunosuppressants<span class="box"></span></span>
    <span>Oral Contraceptive<span class="box"></span></span><span>Other<span class="box"></span></span>
  </div>

  <p class="section-q bold">Please specify medication name, dose, and frequency:</p>
  <div class="med-fields">
    <span class="field"></span><span class="field"></span>
    <span class="field"></span><span class="field"></span>
    <span class="field"></span><span class="field"></span>
  </div>

  <div class="yn-row"><span class="bold">Do you require antibiotic cover?</span><span>Yes<span class="box"></span>No<span class="box"></span></span></div>
  <div class="yn-row"><span class="bold">Have you had a joint replacement?</span><span>Yes<span class="box"></span>No<span class="box"></span></span></div>
  <div class="women">
    <div>Women:</div>
    <div class="yn-row"><span class="bold">Are you pregnant?</span><span>Yes<span class="box"></span>No<span class="box"></span></span></div>
    <div class="yn-row"><span>or <span class="bold">&nbsp;Breast Feeding?</span></span><span>Yes<span class="box"></span>No<span class="box"></span></span></div>
  </div>
</section>

<section class="page page--history">
  <p class="history-q bold">Do you have, or have you had, any of the following?</p>
  <div class="columns">
    <div>
      <div class="group"><h3>Dental</h3>
        <div class="item"><span>Acid Reflux</span><span class="yn">Yes<span class="box"></span>No<span class="box"></span></span></div>
        <div class="item"><span>Bad Breath/Taste</span><span class="yn">Yes<span class="box"></span>No<span class="box"></span></span></div>
        <div class="item"><span>Bleeding/Swollen/Sore Gums</span><span class="yn">Yes<span class="box"></span>No<span class="box"></span></span></div>
        <div class="item"><span>Blisters/Ulcers in Mouth</span><span class="yn">Yes<span class="box"></span>No<span class="box"></span></span></div>
        <div class="item"><span>Broken tooth/filling</span><span class="yn">Yes<span class="box"></span>No<span class="box"></span></span></div>
        <div class="item"><span>Burning tongue</span><span class="yn">Yes<span class="box"></span>No<span class="box"></span></span></div>
        <div class="item"><span>Dry mouth</span><span class="yn">Yes<span class="box"></span>No<span class="box"></span></span></div>
        <div class="item"><span>Food collection between teeth</span><span class="yn">Yes<span class="box"></span>No<span class="box"></span></span></div>
        <div class="item"><span>Grinding/clenching teeth (day/night)</span><span class="yn">Yes<span class="box"></span>No<span class="box"></span></span></div>
        <div class="item"><span>Loose teeth</span><span class="yn">Yes<span class="box"></span>No<span class="box"></span></span></div>
        <div class="item"><span>Crooked teeth</span><span class="yn">Yes<span class="box"></span>No<span class="box"></span></span></div>
        <div class="item"><span>Discoloured teeth</span><span class="yn">Yes<span class="box"></span>No<span class="box"></span></span></div>
        <div class="item"><span>Sensitivity to Hot/Cold</span><span class="yn">Yes<span class="box"></span>No<span class="box"></span></span></div>
        <div class="item"><span>Tooth pain when chewing</span><span class="yn">Yes<span class="box"></span>No<span class="box"></span></span></div>
        <div class="item"><span>Jaw pain/Fracture</span><span class="yn">Yes<span class="box"></span>No<span class="box"></span></span></div>
        <div class="item"><span>Orthodontic treatment/history</span><span class="yn">Yes<span class="box"></span>No<span class="box"></span></span></div>
        <div class="item"><span>Oral Cancer</span><span class="yn">Yes<span class="box"></span>No<span class="box"></span></span></div>
      </div>
      <div class="group"><h3>Diet/Lifestyle</h3>
        <div class="item"><span style="letter-spacing:-.3px">Drink more than one glass alcohol per day</span><span class="yn">Yes<span class="box"></span>No<span class="box"></span></span></div>
        <div class="item"><span>Smoking</span><span class="yn">Yes<span class="box"></span>No<span class="box"></span></span></div>
        <div class="item"><span>Carbonated drinks</span><span class="yn">Yes<span class="box"></span>No<span class="box"></span></span></div>
        <div class="item"><span>Sugary foods</span><span class="yn">Yes<span class="box"></span>No<span class="box"></span></span></div>
      </div>
      <div class="group"><h3>Infectious Disease</h3>
        <div class="item"><span>Creutzfeldt-Jakob Disease</span><span class="yn">Yes<span class="box"></span>No<span class="box"></span></span></div>
        <div class="item"><span>Hepatitis A,B,C,D</span><span class="yn">Yes<span class="box"></span>No<span class="box"></span></span></div>
        <div class="item"><span>HIV/AIDS</span><span class="yn">Yes<span class="box"></span>No<span class="box"></span></span></div>
        <div class="item"><span>Influenza</span><span class="yn">Yes<span class="box"></span>No<span class="box"></span></span></div>
        <div class="item"><span>Shingles</span><span class="yn">Yes<span class="box"></span>No<span class="box"></span></span></div>
        <div class="item"><span>Tuberculosis</span><span class="yn">Yes<span class="box"></span>No<span class="box"></span></span></div>
      </div>
    </div>
    <div>
      <div class="group"><h3>Heart</h3>
        <div class="item"><span>Angina</span><span class="yn">Yes<span class="box"></span>No<span class="box"></span></span></div>
        <div class="item"><span>Atrial Fibrillation</span><span class="yn">Yes<span class="box"></span>No<span class="box"></span></span></div>
        <div class="item"><span>Blood Pressure (High/Low)</span><span class="yn">Yes<span class="box"></span>No<span class="box"></span></span></div>
        <div class="item"><span>Congenital Heart Disease</span><span class="yn">Yes<span class="box"></span>No<span class="box"></span></span></div>
        <div class="item"><span>Heart attack</span><span class="yn">Yes<span class="box"></span>No<span class="box"></span></span></div>
        <div class="item"><span>Heart murmur</span><span class="yn">Yes<span class="box"></span>No<span class="box"></span></span></div>
        <div class="item"><span>Heart surgery</span><span class="yn">Yes<span class="box"></span>No<span class="box"></span></span></div>
        <div class="item"><span>Heart valve replacement</span><span class="yn">Yes<span class="box"></span>No<span class="box"></span></span></div>
        <div class="item"><span>Infective endocarditis</span><span class="yn">Yes<span class="box"></span>No<span class="box"></span></span></div>
        <div class="item"><span>Rheumatic Heart Disease</span><span class="yn">Yes<span class="box"></span>No<span class="box"></span></span></div>
        <div class="item"><span>Pacemaker</span><span class="yn">Yes<span class="box"></span>No<span class="box"></span></span></div>
        <div class="item"><span>Stent</span><span class="yn">Yes<span class="box"></span>No<span class="box"></span></span></div>
      </div>
      <div class="group"><h3>Other</h3>
        <div class="item"><span>Anxiety/PTSD</span><span class="yn">Yes<span class="box"></span>No<span class="box"></span></span></div>
        <div class="item"><span>Arthritis</span><span class="yn">Yes<span class="box"></span>No<span class="box"></span></span></div>
        <div class="item"><span>Alzheimer's</span><span class="yn">Yes<span class="box"></span>No<span class="box"></span></span></div>
        <div class="item"><span>Asthma</span><span class="yn">Yes<span class="box"></span>No<span class="box"></span></span></div>
        <div class="item"><span>Anaphylaxis</span><span class="yn">Yes<span class="box"></span>No<span class="box"></span></span></div>
        <div class="item"><span>Auto-immune disease</span><span class="yn">Yes<span class="box"></span>No<span class="box"></span></span></div>
        <div class="item"><span>Coeliac</span><span class="yn">Yes<span class="box"></span>No<span class="box"></span></span></div>
        <div class="item"><span>Depression</span><span class="yn">Yes<span class="box"></span>No<span class="box"></span></span></div>
        <div class="item"><span>Diabetes</span><span class="yn">Yes<span class="box"></span>No<span class="box"></span></span></div>
        <div class="item"><span>Epilepsy</span><span class="yn">Yes<span class="box"></span>No<span class="box"></span></span></div>
        <div class="item"><span>Kidney Disease</span><span class="yn">Yes<span class="box"></span>No<span class="box"></span></span></div>
        <div class="item"><span>Liver Disease</span><span class="yn">Yes<span class="box"></span>No<span class="box"></span></span></div>
        <div class="item"><span>Osteoporosis</span><span class="yn">Yes<span class="box"></span>No<span class="box"></span></span></div>
        <div class="item"><span>Parkinson's</span><span class="yn">Yes<span class="box"></span>No<span class="box"></span></span></div>
        <div class="item"><span>Radiation to Head/Neck</span><span class="yn">Yes<span class="box"></span>No<span class="box"></span></span></div>
        <div class="item"><span>Schizophrenia</span><span class="yn">Yes<span class="box"></span>No<span class="box"></span></span></div>
        <div class="item"><span>Snoring</span><span class="yn">Yes<span class="box"></span>No<span class="box"></span></span></div>
        <div class="item"><span>Sleep apnea</span><span class="yn">Yes<span class="box"></span>No<span class="box"></span></span></div>
        <div class="item"><span>Stroke</span><span class="yn">Yes<span class="box"></span>No<span class="box"></span></span></div>
        <div class="other-line">Other:<span class="field"></span></div>
      </div>
    </div>
  </div>

  <div class="sign">
    <div class="row"><span class="label">Signature:</span><span class="field"></span></div>
    <div class="row"><span class="label">Date:</span><span class="field"></span></div>
    <div class="row"><span class="label"></span><span class="field"></span></div>
  </div>
  <p class="thanks">Thank you for the time to complete your medical history form. Oral health is linked to overall health and this comprehensive questionnaire will help us to provide you with optimal and safe care.</p>
</section>

</body>
</html>
```